Jewelry Business card for general purpose. Elegant and simple

We are a jewelry group with 6 stores in Mexico and 30 years in business.

We need a BC that at leats includes the name, mail, phone number and physical location (street, municipality, and county; example "Paseo Olmeda 2140", "Avenida Sotillo", "Monterrey").
Optional: we are trying to reposition the brand with the association of life-events or moments and family. Such as: birth, marriage, graduation, birthdays. Christmast, mothers day and fathers day.

We are looking for something elegant but simple

Jewelry name: "Lunetti". Email: "lunettibrillo@correo-ejemplo.mx". Phone num "4172-3095".

Target Market(s)

General business card: from suppliers to clients. One segment outstand: couples gettineg married

Industry/Entity Type

Jewelry Store

Contact Information for Business Card

Loking for something simple but elegant.

Font styles to use
Decorative
Script

Requirements
Must have
• Must have name, address, and mail.
Nice to have
• It could have jewelry pictures/design. Maybe quotes. Or general words as background . currently we have a very simple card with one ring would like to see something different.
Should not have
• Include real people.

```html
<!DOCTYPE html>
<html lang="es">
<head>
<meta charset="utf-8">
<title>Joyeria Lunetti – Tarjeta de presentación</title>
<link rel="stylesheet" href="https://fonts.googleapis.com/css2?family=Abril+Fatface&family=Open+Sans:wght@300;400&display=swap">
<style>
  :root {
    --backdrop: #e9e6e1;
    --card: #ffffff;
    --ink: #111111;
    --ink-soft: #3a3a3a;
    --flourish: #ececec;
    --flourish-edge: rgba(255, 255, 255, 0);
    --card-shadow: rgba(0, 0, 0, 0.18);
  }

  * { box-sizing: border-box; margin: 0; padding: 0; }

  html, body {
    width: 1200px;
    height: 1023px;
    overflow: hidden;
    background: var(--backdrop);
  }

  .stage {
    width: 1200px;
    height: 1023px;
    display: flex;
    align-items: center;
    justify-content: center;
  }

  .business-card {
    position: relative;
    width: 840px;
    height: 480px;
    background: var(--card);
    box-shadow: 0 10px 30px var(--card-shadow);
    overflow: hidden;
  }

  .flourish {
    position: absolute;
    inset: 40px 60px 30px 120px;
    background:
      radial-gradient(ellipse at 55% 35%, var(--flourish) 0%, var(--flourish-edge) 55%),
      radial-gradient(ellipse at 25% 75%, var(--flourish) 0%, var(--flourish-edge) 45%),
      radial-gradient(ellipse at 85% 20%, var(--flourish) 0%, var(--flourish-edge) 35%);
  }

  .card-content {
    position: relative;
    height: 100%;
    display: flex;
    flex-direction: column;
    justify-content: center;
    padding: 0 70px 0 80px;
  }

  .brand-name {
    font-family: "Abril Fatface", "Playfair Display", serif;
    font-weight: 400;
    font-size: 82px;
    line-height: 1;
    letter-spacing: 1px;
    color: var(--ink);
    margin-bottom: 38px;
  }

  .contact {
    list-style: none;
    margin-left: 200px;
    font-family: "Open Sans", Arial, sans-serif;
    font-weight: 300;
    font-size: 21px;
    line-height: 1.55;
    color: var(--ink-soft);
  }

  .contact .locality {
    padding-left: 150px;
  }
</style>
</head>
<body>
  <main class="stage">
    <article class="business-card">
      <div class="flourish" role="img" aria-label="Faint grey floral flourish ornament in the card background"></div>
      <div class="card-content">
        <h1 class="brand-name">Joyeria Lunetti</h1>
        <ul class="contact">
          <li class="phone">4172-3095</li>
          <li class="email">lunettibrillo@correo-ejemplo.mx</li>
          <li class="street">Paseo Olmeda 2140, Avenida Sotillo,</li>
          <li class="locality">Monterrey</li>
        </ul>
      </div>
    </article>
  </main>
</body>
</html>
```